San Francisco Pet Care Non Profit

Business Card Design for non profit organization.
We are a mobile pet care team who supports and attends to pets whose owners are homeless. Thanks for your help and creativity.

Industry/Entity Type

Non Profit

Contact Information for Business Card

Marisol Keddy
President
2871 Larkmoor Street, #512
San Francisco, CA 94187
phone: 415-729-3846
fax: 415-781-4052
marisol@tidywagonvan.org
website: tidywagonvan.org
facebook: facebook.com/TidyWagonVan

Font styles to use
Serif
Sans Serif

Colors

Designer to choose colors to be used in the design.

Requirements
Must have
• above details and attached logo

```html
<!DOCTYPE html>
<html lang="en">
<head>
<meta charset="utf-8">
<title>TidyWagonVan – Business Card</title>
<link href="https://fonts.googleapis.com/css2?family=Arimo:wght@400;700&display=swap" rel="stylesheet">
<style>
  :root {
    --brand-blue: #29a8e0;
    --brand-blue-soft: #d7eefa;
    --ink: #1b1b1b;
    --paper: #ffffff;
    --backdrop: #ecebe8;
    --watermark: rgba(255,255,255,0.14);
  }
  * { margin: 0; padding: 0; box-sizing: border-box; }
  html, body { width: 900px; height: 1200px; overflow: hidden; }
  body {
    background: var(--backdrop);
    font-family: "Arimo", Arial, sans-serif;
    position: relative;
  }
  .card {
    position: absolute;
    left: 88px;
    width: 734px;
    height: 430px;
    border-radius: 22px;
    overflow: hidden;
    box-shadow: 0 4px 14px rgba(0,0,0,0.18);
  }
  /* Front */
  .card-front { top: 125px; background: var(--paper); }
  .van-illustration {
    position: absolute; left: 512px; top: 14px; width: 222px; height: 404px;
    background: linear-gradient(180deg, var(--brand-blue-soft), #eef6fb);
    border-radius: 60px 0 0 30px;
    z-index: 0;
  }
  .front-text { position: relative; z-index: 1; }
  .brand-name {
    position: absolute; left: 38px; top: 52px;
    font-size: 45px; font-weight: 700; color: var(--brand-blue);
    letter-spacing: -0.3px; white-space: nowrap;
  }
  .brand-tagline {
    position: absolute; left: 85px; top: 103px;
    font-size: 19px; font-weight: 700; color: var(--ink);
    white-space: nowrap;
  }
  .person-name {
    position: absolute; left: 38px; top: 158px;
    font-size: 24px; font-weight: 700; color: var(--ink);
    white-space: nowrap;
  }
  .person-role {
    position: absolute; left: 38px; top: 186px;
    font-size: 16px; font-weight: 700; color: var(--brand-blue);
  }
  .contact-list { position: absolute; left: 38px; top: 223px; list-style: none; }
  .contact-item {
    display: flex; align-items: center; height: 29.3px;
    font-size: 16px; font-weight: 700; color: var(--ink);
    white-space: nowrap;
  }
  .contact-item.address { letter-spacing: -0.2px; }
  .contact-icon {
    width: 20px; height: 20px; margin-right: 14px; flex: none;
  }
  .contact-item.social { color: var(--brand-blue); }
  /* Back */
  .card-back { top: 640px; background: var(--brand-blue); }
  .mark-watermark {
    position: absolute; left: 467px; top: 0; width: 267px; height: 430px;
    background: var(--watermark);
    border-radius: 90px 0 0 0;
  }
  .back-lockup { position: absolute; left: 152px; top: 162px; display: flex; align-items: center; z-index: 1; }
  .lockup-dot {
    width: 70px; height: 70px; border-radius: 50%;
    background: var(--paper); margin-right: 24px; flex: none;
  }
  .back-name { font-size: 50px; font-weight: 700; color: var(--paper); line-height: 1; white-space: nowrap; }
  .back-tagline {
    font-size: 19px; font-weight: 700; color: var(--paper);
    margin-left: 52px; margin-top: 6px; white-space: nowrap;
  }
  .back-url {
    position: absolute; left: 0; width: 734px; text-align: center; top: 365px;
    font-size: 16px; font-weight: 700; color: var(--paper);
    padding-right: 6px; z-index: 1;
  }
</style>
</head>
<body>

<section class="card card-front">
  <div class="van-illustration" role="img" aria-label="Brand illustration: a cat and a dog forming a heart riding a small van"></div>

  <div class="front-text">
    <div class="brand-name">TidyWagonVan</div>
    <div class="brand-tagline">Mobile Pet Care Team</div>

    <div class="person-name">Marisol Keddy</div>
    <div class="person-role">President</div>

    <ul class="contact-list">
      <li class="contact-item">
        <svg class="contact-icon" viewBox="0 0 20 20"><circle cx="10" cy="10" r="10" fill="var(--brand-blue)"/><path d="M6.5 5.5l2 0 1 2.5-1.3 1a6 6 0 0 0 2.8 2.8l1-1.3 2.5 1v2c-4.5.4-8.4-3.5-8-8z" fill="#fff"/></svg>
        415-729-3846
      </li>
      <li class="contact-item">
        <svg class="contact-icon" viewBox="0 0 20 20"><circle cx="10" cy="10" r="10" fill="var(--brand-blue)"/><rect x="7" y="5" width="6" height="3" fill="#fff"/><rect x="5" y="8" width="10" height="5" rx="1" fill="#fff"/><rect x="7" y="11" width="6" height="4" fill="#fff" stroke="var(--brand-blue)" stroke-width="0.8"/></svg>
        415-781-4052
      </li>
      <li class="contact-item">
        <svg class="contact-icon" viewBox="0 0 20 20"><circle cx="10" cy="10" r="10" fill="var(--brand-blue)"/><rect x="5" y="6.5" width="10" height="7" fill="#fff"/><path d="M5 6.5l5 4 5-4" fill="none" stroke="var(--brand-blue)" stroke-width="1"/></svg>
        marisol@tidywagonvan.org
      </li>
      <li class="contact-item">
        <svg class="contact-icon" viewBox="0 0 20 20"><circle cx="10" cy="10" r="10" fill="var(--brand-blue)"/><g fill="none" stroke="#fff" stroke-width="1.1"><circle cx="10" cy="10" r="5"/><ellipse cx="10" cy="10" rx="2.2" ry="5"/><path d="M5 10h10M6 7.5h8M6 12.5h8"/></g></svg>
        www.tidywagonvan.org
      </li>
      <li class="contact-item social">
        <svg class="contact-icon" viewBox="0 0 20 20"><circle cx="10" cy="10" r="10" fill="var(--brand-blue)"/></svg>
        TidyWagonVan
      </li>
      <li class="contact-item address">
        <svg class="contact-icon" viewBox="0 0 20 20"><circle cx="10" cy="10" r="10" fill="var(--brand-blue)"/><path d="M10 4a4 4 0 0 1 4 4c0 3-4 8-4 8s-4-5-4-8a4 4 0 0 1 4-4z" fill="#fff"/><circle cx="10" cy="8" r="1.5" fill="var(--brand-blue)"/></svg>
        2871 Larkmoor Street, #512, San Francisco, CA 94187
      </li>
    </ul>
  </div>
</section>

<section class="card card-back">
  <div class="mark-watermark" role="img" aria-label="Faint large brand illustration in the corner"></div>
  <div class="back-lockup">
    <div class="lockup-dot"></div>
    <div>
      <div class="back-name">TidyWagonVan</div>
      <div class="back-tagline">Mobile Pet Care Team</div>
    </div>
  </div>
  <div class="back-url">www.tidywagonvan.org</div>
</section>

</body>
</html>
```